3 pages of UI design for AdTech Startup

We need 3 pages of UI design for a new AdTech company located in Seattle called KESTREL Systems.

We put digital, mobile billboards on college campuses throughout the country. This design project involves our back-end customer dashboard.

Page 1- Dashboard home page
page 2- Manage ads screen (see File 3 below for the screenshot of our current design). Please match the design of all 3 screens so there is consistency
page 3-Detailed Zone screen (see file 16 below). This page looks similar to the first page but gives a more detailed overview and a larger map.

The features and functionality are already built but we are lacking an aesthetically pleasing and slick design. Looking for someone who can match our website look to this new dashboard space. Our company reflects modern, clean, elegant design that is straight-forward and user friendly (main inspiration is VOLTA, we love their design and feel).

Target Market(s)

-Local business owner, marketing directors, and national advertising and marketing agencies

Industry/Entity Type

Advertising

Number of Pages Required

3 page

Font styles to use
Other font styles liked:
• Proxima Nova- Thin for body text, Light for title

Colors
85cae6
33a6d7
0292cd
ffffff

Requirements
Nice to have
• Please include enough detail so that my developer can look at the design you come up with and translate it to html. Please include spacing, fonts, color numbers. My developer is going to look at your creation and recreate it in html format

```html
<!DOCTYPE html>
<html lang="en">
<head>
<meta charset="utf-8">
<title>KESTREL Systems – Insights Summary</title>
<link rel="stylesheet" href="https://fonts.googleapis.com/css2?family=Montserrat:wght@300;400;500;600;700&display=swap">
<style>
  :root{
    --bg:#f4f4f4;
    --white:#ffffff;
    --cyan:#00bfea;
    --green:#00a65a;
    --orange:#f8a031;
    --coral:#ff6b57;
    --brand:#33a6d7;
    --brand-light:#85cae6;
    --line:#e6e6e6;
    --grid:#ececec;
    --ink:#333333;
    --muted:#8e8e8e;
    --footer:#000000;
  }
  *{box-sizing:border-box;margin:0;padding:0}
  html,body{width:1200px;height:935px;overflow:hidden}
  body{position:relative;background:var(--bg);font-family:"Montserrat",sans-serif;color:var(--ink)}

  /* header */
  .topbar{position:absolute;left:0;top:0;width:1200px;height:100px;background:var(--white);border-top:2px solid var(--brand);box-shadow:0 1px 3px rgba(0,0,0,.06)}
  .brand{position:absolute;left:99px;top:33px;display:flex;align-items:center;gap:10px}
  .brand-dot{width:30px;height:30px;border-radius:50%;background:var(--brand)}
  .brand-name{font-size:24px;font-weight:400;letter-spacing:1px;color:var(--brand)}
  .nav{position:absolute;right:100px;top:24px;height:48px;display:flex;align-items:center;font-size:14px;font-weight:500;color:var(--ink)}
  .nav-divider{width:1px;height:16px;background:#cfcfcf;margin:0 14px}
  .avatar{width:47px;height:47px;border-radius:50%;background:linear-gradient(135deg,#6b4a3a,#c9a48b)}
  .user-name{margin-left:14px}
  .caret{margin-left:18px;width:0;height:0;border-left:5px solid transparent;border-right:5px solid transparent;border-top:5px solid var(--ink)}
  .help{display:flex;align-items:center;gap:8px}

  /* panels */
  .panel{position:absolute;background:var(--white);border:1px solid var(--line)}
  .chart-panel{left:99px;top:126px;width:731px;height:461px}
  .date-range{position:absolute;left:60px;top:26px;width:206px;height:33px;background:var(--coral);color:var(--white);font-size:12px;display:flex;align-items:center;justify-content:center}
  .range-tabs{position:absolute;left:427px;top:26px;display:flex;height:33px}
  .range-tabs span{width:62.7px;display:flex;align-items:center;justify-content:center;color:var(--white);font-size:12px}
  .tab-hourly{background:var(--cyan)}
  .tab-day{background:var(--green)}
  .tab-week{background:var(--orange)}
  .tab-month{background:var(--coral)}
  .plot{position:absolute;left:60px;top:80px}
  .y-label{position:absolute;right:681px;font-size:11px;color:#555}
  .x-label{position:absolute;top:418px;font-size:11px;color:var(--muted);transform:translateX(-50%);white-space:nowrap}

  .stats{position:absolute;left:856px;width:244px;background:var(--white);border:1px solid var(--line)}
  .stats-top{top:126px;height:461px}
  .stat-row{height:43px;display:flex;align-items:center;justify-content:center;font-size:12.5px;color:var(--white);border-bottom:1px solid var(--line)}
  .stat-row b{font-weight:600;margin-right:4px}
  .stat-row span{font-weight:300}
  .row-cyan{background:var(--cyan);border-color:var(--cyan)}
  .row-green{background:var(--green);border-color:var(--green)}
  .row-orange{background:var(--orange);border-color:var(--orange)}
  .row-coral{background:var(--coral);border-color:var(--coral)}

  .card{position:absolute;top:614px;height:247px;background:var(--white);border:1px solid var(--line)}
  .card-head{height:43px;display:flex;align-items:center;justify-content:center;color:var(--white);font-size:16px;font-weight:600}
  .zone-card{left:99px;width:110px}
  .zone-name{margin-top:10px;text-align:center;font-size:13px;font-weight:600;text-decoration:underline}
  .zone-place{margin-top:8px;text-align:center;font-size:12px}
  .ad-card{left:236px;width:206px}
  .ad-media{position:absolute;left:8px;top:53px;width:190px;height:186px;border:1px solid var(--orange);background:linear-gradient(180deg,#4a2a2a 0%,#7a4a3a 45%,#b07a4a 70%,#5b3f7a 100%)}
  .paths-card{left:469px;width:361px}
  .paths-map{position:absolute;left:8px;top:53px;width:345px;height:185px;border:1px solid #bbb;background:linear-gradient(160deg,#4f5e3f 0%,#6b7451 50%,#596648 100%)}

  .stats-bottom{top:614px;height:247px}
  .messages{height:67px;padding:16px 0 0 16px;font-size:11px;color:#555;border-bottom:1px solid var(--line)}
  .details-btn{display:block;margin:14px auto 0;width:75px;height:25px;border-radius:13px;background:var(--coral);color:var(--white);font-size:11px;font-weight:500;display:flex;align-items:center;justify-content:center}

  .footer{position:absolute;left:0;top:888px;width:1200px;height:47px;background:var(--footer);color:var(--white);font-size:13px;font-weight:500;display:flex;align-items:center;justify-content:center}
</style>
</head>
<body>
  <header class="topbar">
    <div class="brand"><div class="brand-dot"></div><div class="brand-name">KESTREL</div></div>
    <nav class="nav">
      <span>Insights Summary</span>
      <span class="nav-divider"></span>
      <div class="avatar" role="img" aria-label="User profile photo"></div>
      <span class="user-name">Reed Calloway</span>
      <span class="caret"></span>
      <span class="nav-divider"></span>
      <span class="help">
        <svg width="19" height="19" viewBox="0 0 20 20"><circle cx="10" cy="10" r="9" fill="none" stroke="#33a6d7" stroke-width="1.6"/><path d="M5 6c2 1 3 0 4 2s-1 3 1 4 1 4 1 4M13 3c0 2 2 2 3 4" fill="none" stroke="#33a6d7" stroke-width="1.4"/></svg>
        Help
      </span>
    </nav>
  </header>

  <section class="panel chart-panel">
    <div class="date-range">29 July2016 - 05 Aug2016</div>
    <div class="range-tabs">
      <span class="tab-hourly">Hourly</span><span class="tab-day">Day</span><span class="tab-week">Week</span><span class="tab-month">Month</span>
    </div>

    <svg class="plot" width="618" height="320" viewBox="0 0 618 320">
      <rect x="0" y="0" width="618" height="319" fill="#fbfbfb"/>
      <polygon points="0,170 88,185 265,80 353,150 442,40 618,65 618,319 0,319" fill="#f4f4f4"/>
      <g stroke="var(--grid)" stroke-width="1.5">
        <line x1="0" y1="0" x2="0" y2="319"/><line x1="88" y1="0" x2="88" y2="319"/><line x1="177" y1="0" x2="177" y2="319"/><line x1="265" y1="0" x2="265" y2="319"/><line x1="353" y1="0" x2="353" y2="319"/><line x1="441" y1="0" x2="441" y2="319"/><line x1="530" y1="0" x2="530" y2="319"/><line x1="617" y1="0" x2="617" y2="319"/>
        <line x1="0" y1="1" x2="618" y2="1"/><line x1="0" y1="39" x2="618" y2="39"/><line x1="0" y1="80" x2="618" y2="80"/><line x1="0" y1="119" x2="618" y2="119"/><line x1="0" y1="159" x2="618" y2="159"/><line x1="0" y1="198" x2="618" y2="198"/><line x1="0" y1="238" x2="618" y2="238"/><line x1="0" y1="277" x2="618" y2="277"/>
      </g>
      <polygon points="0,257 88,290 177,264 265,289 353,211 441,249 530,132 618,291 618,319 0,319" fill="#aee0f3"/>
      <polyline points="0,257 88,290 177,264 265,289 353,211 441,249 530,132 618,291" fill="none" stroke="#3ab4e4" stroke-width="3.5" stroke-linejoin="round"/>
      <line x1="0" y1="318" x2="618" y2="318" stroke="#85cae6" stroke-width="2"/>
      <g fill="#5cc4ee" stroke="#2a9fd0" stroke-width="1">
        <circle cx="88" cy="290" r="7"/><circle cx="177" cy="264" r="7"/><circle cx="265" cy="289" r="7"/><circle cx="353" cy="211" r="7"/><circle cx="441" cy="249" r="7"/><circle cx="530" cy="132" r="7"/>
      </g>
    </svg>

    <span class="y-label" style="top:231px">100</span>
    <span class="y-label" style="top:271px">75</span>
    <span class="y-label" style="top:311px">50</span>
    <span class="y-label" style="top:350px">25</span>
    <span class="y-label" style="top:389px">0</span>

    <span class="x-label" style="left:148px">July 29, 2016</span>
    <span class="x-label" style="left:236px">July 30, 2016</span>
    <span class="x-label" style="left:325px">July 31, 2016</span>
    <span class="x-label" style="left:413px">Aug 01, 2016</span>
    <span class="x-label" style="left:503px">Aug 02, 2016</span>
    <span class="x-label" style="left:593px">Aug 03, 2016</span>
  </section>

  <aside class="stats stats-top">
    <div class="stat-row row-cyan"><b>Rotationsd :</b><span>85</span></div>
    <div class="stat-row row-green"><b>Time :</b><span>21.25 min</span></div>
    <div class="stat-row row-orange"><b>Impressions :</b><span>595</span></div>
    <div class="stat-row row-coral"><b>Miles :</b><span>0.3 miles</span></div>
    <div class="stat-row"></div><div class="stat-row"></div><div class="stat-row"></div><div class="stat-row"></div><div class="stat-row"></div><div class="stat-row"></div>
  </aside>

  <section class="card zone-card">
    <div class="card-head row-green">Zone</div>
    <div class="zone-name">Zone 1</div>
    <div class="zone-place">Marlow's House</div>
  </section>

  <section class="card ad-card">
    <div class="card-head row-orange">Active Ad</div>
    <div class="ad-media" role="img" aria-label="Currently playing ad: basketball game footage"></div>
  </section>

  <section class="card paths-card">
    <div class="card-head row-coral">Carrier Paths</div>
    <div class="paths-map" role="img" aria-label="Satellite map of carrier walking paths"></div>
  </section>

  <aside class="stats stats-bottom">
    <div class="stat-row row-cyan"><b>Rotationsd :</b><span>85</span></div>
    <div class="stat-row row-green"><b>Broadcast Time :</b><span>21.25 min</span></div>
    <div class="stat-row row-orange"><b>Miles Walked :</b><span>0.3 miles</span></div>
    <div class="messages">Text Messages...</div>
    <span class="details-btn">Details</span>
  </aside>

  <footer class="footer">Copyright © 2016&nbsp; Kestrel. All Right Reserved.</footer>
</body>
</html>
```